Bright Path Crest Oak Realty yard sign Logo

UPDATE Design logo for Realty yard sign. 24x24 diamond or 36x24 Rectangle.
Open to all ideas. We are a discount firm but want to project a high end feel. We provide 100% of all services and extensive marketing for 1/2 the fee.
The following info must be on sign
BRIGHT PATH CREST (OR 1/3) OAK REALTY
Tomas Reyne 555-0147
CrestoakQX.com

Target Market(s)

home sellers and buyers

Industry/Entity Type

Real Estate yard sign please see sign attached in gif

Logo Text

Bright Path Crest Oak Realty OR (1/3 IN PLACE OF CREST)

Requirements
Must have
• BRIGHT PATH CREST (OR 1/3) OAK REALTY Tomas Reyne 555-0147 CrestoakQX.com FOR SALE (optional)

```html
<!DOCTYPE html>
<html lang="en">
<head>
<meta charset="utf-8">
<title>Bright Path Crest Oak Realty — Yard Sign</title>
<link rel="stylesheet" href="https://fonts.googleapis.com/css2?family=Montserrat:wght@500;600;800&display=swap">
<style>
  :root {
    --white: #ffffff;
    --black: #000000;
    --paper: #ffffff;
    --divider: #c9c9c9;
    --lawn-top: #8e8f86;
    --lawn-mid: #4f7a2c;
    --lawn-low: #3f7d22;
  }
  * { margin: 0; padding: 0; box-sizing: border-box; }
  html, body { width: 1200px; height: 2325px; overflow: hidden; background: var(--paper); }
  body { position: relative; font-family: "Montserrat", sans-serif; }

  .panel { position: absolute; overflow: hidden; }
  .panel--hero { left: 0; top: 0; width: 1200px; height: 891px; background: var(--white); border-bottom: 2px solid var(--divider); }
  .panel--dark { left: 0; top: 891px; width: 603px; height: 613px; background: var(--black); }
  .panel--light { left: 603px; top: 891px; width: 597px; height: 613px; background: var(--white); }
  .panel--yard { left: 0; top: 1504px; width: 1200px; height: 821px; }

  .yard-photo {
    position: absolute; inset: 0;
    background: linear-gradient(180deg, #d9d9d4 0%, var(--lawn-top) 22%, #6d6a5e 26%, var(--lawn-mid) 34%, var(--lawn-low) 100%);
  }

  .sign { position: absolute; overflow: visible; }
  .sign--hero { left: 339px; top: 184px; width: 522px; height: 522px; }
  .sign--dark { left: 158px; top: 161px; width: 287px; height: 287px; }
  .sign--light { left: 155px; top: 161px; width: 287px; height: 287px; }
  .sign--yard { left: 469px; top: 153px; width: 454px; height: 454px; }

  .theme-gold {
    --outline: #000; --cap: #000; --body: #fff; --ink: #000;
    --band: #000; --band-ink: url(#gold); --strip: #fff; --strip-ink: url(#gold); --base: #000;
  }
  .theme-night {
    --outline: #fff; --cap: #fff; --body: #000; --ink: #fff;
    --band: #fff; --band-ink: url(#gold); --strip: #000; --strip-ink: url(#gold); --base: #fff;
  }
  .theme-mono {
    --outline: #000; --cap: #000; --body: #fff; --ink: #000;
    --band: #000; --band-ink: #fff; --strip: #fff; --strip-ink: #000; --base: #000;
  }

  .sign-outline { fill: var(--body); stroke: var(--outline); stroke-width: 4; }
  .sign-body { fill: var(--body); }
  .sign-cap { fill: var(--cap); }
  .sign-band { fill: var(--band); }
  .sign-strip { fill: var(--strip); }
  .sign-base { fill: var(--base); }
  .sign-rule { stroke: var(--ink); stroke-width: 2; }
  .sign-for-sale { fill: var(--ink); font-weight: 500; font-size: 22px; letter-spacing: 5px; }
  .sign-brand { fill: var(--ink); font-weight: 800; }
  .sign-brand--main { font-size: 40px; letter-spacing: -1px; }
  .sign-brand--sub { font-size: 19px; letter-spacing: 3px; }
  .sign-web { fill: var(--ink); font-weight: 600; font-size: 12px; letter-spacing: 3.5px; }
  .sign-agent { fill: var(--band-ink); font-weight: 800; font-size: 34px; letter-spacing: -0.5px; }
  .sign-phone { fill: var(--strip-ink); font-weight: 800; font-size: 22px; letter-spacing: 9px; }
</style>
</head>
<body>

<svg width="0" height="0" style="position:absolute" aria-hidden="true">
  <defs>
    <linearGradient id="gold" x1="0" y1="0" x2="1" y2="1">
      <stop offset="0" stop-color="#8a6a1c"/>
      <stop offset="0.45" stop-color="#f7e27c"/>
      <stop offset="0.7" stop-color="#c99a2e"/>
      <stop offset="1" stop-color="#7d5e16"/>
    </linearGradient>
    <clipPath id="sign-clip">
      <polygon points="220,10 430,220 220,430 10,220"/>
    </clipPath>
    <path id="sale-arc" d="M 128 140 A 95 95 0 0 1 312 140"/>
    <symbol id="yard-sign" viewBox="0 0 440 440">
      <polygon class="sign-outline" points="220,2 438,220 220,438 2,220"/>
      <g clip-path="url(#sign-clip)">
        <rect class="sign-body" x="0" y="0" width="440" height="440"/>
        <path class="sign-cap" d="M 0 0 H 440 V 78 L 300 78 Q 220 -6 140 78 L 0 78 Z"/>
        <rect class="sign-band" x="0" y="265" width="440" height="48"/>
        <rect class="sign-strip" x="0" y="313" width="440" height="39"/>
        <rect class="sign-base" x="0" y="352" width="440" height="88"/>
      </g>
      <text class="sign-for-sale" text-anchor="middle"><textPath href="#sale-arc" startOffset="50%">FOR SALE</textPath></text>
      <text class="sign-brand sign-brand--main" x="220" y="180" text-anchor="middle">Bright Path</text>
      <text class="sign-brand sign-brand--sub" x="220" y="210" text-anchor="middle">CREST OAK REALTY</text>
      <line class="sign-rule" x1="80" y1="248" x2="118" y2="248"/>
      <line class="sign-rule" x1="322" y1="248" x2="360" y2="248"/>
      <text class="sign-web" x="220" y="252" text-anchor="middle">CRESTOAKQX.COM</text>
      <text class="sign-agent" x="220" y="302" text-anchor="middle">TOMAS REYNE</text>
      <text class="sign-phone" x="224" y="341" text-anchor="middle">555-0147</text>
    </symbol>
  </defs>
</svg>

<section class="panel panel--hero">
  <svg class="sign sign--hero theme-gold" viewBox="0 0 440 440" role="img" aria-label="Bright Path Crest Oak Realty for sale sign"><use href="#yard-sign"/></svg>
</section>

<section class="panel panel--dark">
  <svg class="sign sign--dark theme-night" viewBox="0 0 440 440" role="img" aria-label="Sign on black"><use href="#yard-sign"/></svg>
</section>

<section class="panel panel--light">
  <svg class="sign sign--light theme-mono" viewBox="0 0 440 440" role="img" aria-label="Single colour sign"><use href="#yard-sign"/></svg>
</section>

<section class="panel panel--yard">
  <div class="yard-photo" role="img" aria-label="Front yard with green lawn, white porch railing, house siding and potted yellow flowers"></div>
  <svg class="sign sign--yard theme-gold" viewBox="0 0 440 440" role="img" aria-label="Sign standing in the yard"><use href="#yard-sign"/></svg>
</section>

</body>
</html>
```